Ridgefall Stoneworks Business card logo

We are a tile and natural stone installation company with an emphasis on high quality and design assistance. I prefer a black background with a graphic logo or maybe a photo that gives a feel of tile/natural stone. I like bold, but tasteful colors. Something to really catch the eye without being gaudy. The final design should convey expert quality and attention to detail.

Contact Information for Business Card

RIDGEFALL STONEWORKS Quality Design and Installation

Other font styles liked:
• Graviton, Illegal curves

Requirements
Must have
• Business card must be an eye-catcher, but tasteful.
• Information I need on the card:
• Business name and tagline
• Warren Pelsby, owner
• Phone: (xxx) xxx-xxxx
• Email
• Website

```html
<!DOCTYPE html>
<html lang="en">
<head>
<meta charset="utf-8">
<title>Ridgefall Stoneworks – Business Card</title>
<link rel="stylesheet" href="https://fonts.googleapis.com/css2?family=Open+Sans:wght@400;600;700&family=Alegreya+Sans:ital@1&display=swap">
<style>
  :root {
    --backdrop: #e8e8e9;
    --card: #f5f5f5;
    --navy: #4b4b74;
    --navy-ink: #2c2c48;
    --terracotta: #c2694c;
    --terracotta-light: #d8876b;
    --slate: #6c6c80;
    --white: #ffffff;
  }
  * { box-sizing: border-box; margin: 0; padding: 0; }
  html, body { width: 1200px; height: 720px; overflow: hidden; }
  body {
    background: var(--backdrop);
    font-family: "Open Sans", Arial, sans-serif;
    position: relative;
  }
  .card {
    position: absolute;
    top: 195px;
    width: 530px;
    height: 310px;
    background: var(--card);
    overflow: hidden;
    box-shadow: 0 2px 6px rgba(0,0,0,0.12);
  }
  .card--back { left: 55px; }
  .card--front { left: 615px; }

  .wordmark {
    position: absolute;
    display: flex;
    align-items: center;
    gap: 12px;
    font-weight: 700;
    color: var(--navy);
    text-transform: uppercase;
    letter-spacing: 0.5px;
    line-height: 1;
    white-space: nowrap;
  }
  .wordmark__square {
    width: 22px; height: 22px;
    background: var(--terracotta);
    flex: none;
  }
  .tagline {
    position: absolute;
    font-family: "Alegreya Sans", Georgia, sans-serif;
    font-style: italic;
    color: var(--slate);
    white-space: nowrap;
  }

  /* contact side */
  .card--back .wordmark { left: 34px; top: 48px; font-size: 30px; }
  .card--back .tagline { left: 70px; top: 96px; font-size: 19px; }

  .contact-band {
    position: absolute;
    left: 0; right: 0;
    top: 146px; bottom: 0;
    background: var(--terracotta);
    border-top: 4px solid var(--navy);
  }
  .name-panel {
    position: absolute;
    left: 0; top: 200px; bottom: 0;
    width: 230px;
    background: var(--navy);
    border-top: 4px solid var(--terracotta-light);
    color: var(--white);
    padding: 26px 0 0 30px;
  }
  .name-panel__name { font-size: 25px; font-weight: 400; line-height: 1.2; }
  .name-panel__role { font-size: 15px; margin-top: 2px; }

  .contact-list {
    position: absolute;
    left: 244px; top: 166px;
    list-style: none;
  }
  .contact-list li {
    display: flex;
    align-items: center;
    height: 32px;
    color: var(--navy-ink);
    font-size: 16px;
    font-weight: 600;
    white-space: nowrap;
  }
  .contact-icon {
    width: 22px; height: 22px;
    background: var(--terracotta-light);
    margin-right: 12px;
    display: flex; align-items: center; justify-content: center;
    flex: none;
  }

  /* logo side */
  .card--front .wordmark { left: 56px; top: 118px; font-size: 32px; }
  .card--front .tagline { left: 100px; top: 170px; font-size: 21px; }
</style>
</head>
<body>

  <section class="card card--back" aria-label="Business card, contact side">
    <div class="wordmark"><span class="wordmark__square"></span>Ridgefall Stoneworks</div>
    <p class="tagline">Quality Design and Installation</p>

    <div class="contact-band"></div>

    <ul class="contact-list">
      <li>
        <span class="contact-icon">
          <svg width="10" height="14" viewBox="0 0 10 14"><rect x="1" y="0.5" width="8" height="13" rx="1.5" fill="none" stroke="#fff" stroke-width="1.2"/><circle cx="5" cy="11" r="0.9" fill="#fff"/></svg>
        </span>Phone Number here
      </li>
      <li>
        <span class="contact-icon">
          <svg width="14" height="10" viewBox="0 0 14 10"><rect x="0.6" y="0.6" width="12.8" height="8.8" fill="none" stroke="#fff" stroke-width="1.2"/><path d="M0.6 0.6 L7 5.6 L13.4 0.6" fill="none" stroke="#fff" stroke-width="1.2"/></svg>
        </span>Email address
      </li>
      <li>
        <span class="contact-icon">
          <svg width="13" height="13" viewBox="0 0 13 13"><circle cx="6.5" cy="6.5" r="5.6" fill="none" stroke="#fff" stroke-width="1.1"/><ellipse cx="6.5" cy="6.5" rx="2.4" ry="5.6" fill="none" stroke="#fff" stroke-width="1"/><path d="M0.9 6.5 H12.1" stroke="#fff" stroke-width="1"/></svg>
        </span>website address
      </li>
    </ul>

    <div class="name-panel">
      <p class="name-panel__name">Name here</p>
      <p class="name-panel__role">Position</p>
    </div>
  </section>

  <section class="card card--front" aria-label="Business card, logo side">
    <div class="wordmark"><span class="wordmark__square"></span>Ridgefall Stoneworks</div>
    <p class="tagline">Quality Design and Installation</p>
  </section>

</body>
</html>
```